Colourful Bold Design for Pet Insurance Website

PLEASE NOTE THAT THIS PROJECT HAS BEEN EXTENDED. Please read the PROJECT EXTENSION DOCUMENT BEFORE STARTING WORK ON ANY DESIGNS.

We are looking for a colourful bold new template design for our JOOMLA HOMEPAGE and a matching design for our new WORDPRESS BLOG.

The website will help pet owners work out which insurance policy best meets their needs. The aim of the website is to explain policy differences in a plain clear manner.

The website will need to have a professional colourful image. It needs to be BOLD, CLEAN AND SHARP rather than soft, pastel and cuddly.

COLOUR SCHEME
The website needs to have a bold colourful design on a white background.
On the inner pages we will have five different types of policies which will be colour coded. We would ideally therefore like to incorporate five distinct colours in the design. See attached document for example of colour schemes we like.

LOGO
We want to keep the existing logo. Please find the file attached. You may though change the logo colours.

CONTENT
One of the reasons for the new design is that we want to change the style of the homepage and include new content. Our current homepage can be found at www.furrow-cover-polls.co.uk.

Content Required
Slideshow
Article Intro.. About Pet Insurance
Policy Lookup Box (see existing site… you can change the design of this)
Six link options (see links on left of current page)
Latest Reviews (List of 6)
Ad (Same dimensions as currently on homepage)

News and Comment Section - To include Three or Four Articles, Title, Intro to article (probably 3 or 4 lines .. about 400px wide), Read more link
Social Media Section
Chatterbook Plugin with Feed
Latest Tweets Plugin
Pet Charities Latest Tweets
Footer
Larger footer with lots of links grouped in sections

It does not need to include the clipart pic of the pets which is on the current homepage.

Examples of Websites and Templates We Like
http://www.pawlane.com/ (like colours… fonts…layout)
http://sitetheme.brightkiln.com/?template=upbeat&path=/... (like the clarity, "white" space etc)
http://www.layoutforge.com/demo/51872.html (like white space, clear easy to read fonts… don’t like colour scheme, size of top picture)
http://www.layoutforge.com/website-templates/63915.html (like colour scheme, use of white space)

FEEDBACK
I will provide lots of feedback on all designs submitted so that together we can get the best result.

For clarification this is a DESIGN ONLY project. Our website developer will view the designs before we make our final choice as he wants to ensure he can develop "sharp, practical and most importantly light weight web interface" from the design.

Just updated this brief to clarify design issues, content issues and to give some more examples of site designs I like. 

Please note that although we wish to keep the logo you can change the colours to suit your design. 

Please note that we have now added details of pictures we would be happy to use on the website.  We would prefer it if you used one of these.   Otherwise please ensure your picture includes a nice dog and nice cat and no people!

I have been delighted with the quality of the designs submitted for this project.  So much so that I am going to extend the project to include some additional inner pages.   The amended brief will be posted on here on Friday 10 May.   The deadline will be extended and the budget will also be increased. 

Reason: Additional inner pages now required. Budget will be increased. Revised brief to be posted on here Friday 10 May.

Target Market(s)

Pet owners in the UK who are confused about pet insurance. It therefore needs to be a bold design which is plain, clean and easy to read. It should use bold colours rather than pastels and should not use "cuddly" images.

Industry/Entity Type

Insurance

Requirements
Must have
• Bold clear and distinct colours (preferably 5)
Content as per uploaded file (not just content from existing site)
Easy to read fonts
Should not have
• Pastel colours
Cuddly images

```html
<!DOCTYPE html>
<html lang="en">
<head>
<meta charset="utf-8">
<title>Furrow Cover Polls UK</title>
<link rel="stylesheet" href="https://fonts.googleapis.com/css2?family=Open+Sans:ital,wght@0,400;0,600;0,700;0,800;1,400&display=swap">
<style>
:root{
  --black:#000;
  --ink:#222;
  --muted:#8a8a8a;
  --teal:#16d6c6;
  --teal-deep:#0f7f86;
  --teal-panel:#2aa7b0;
  --cyan:#15b6e6;
  --magenta:#e6148c;
  --orange:#e8641c;
  --grey:#7a7a7a;
  --dark:#2a2a2a;
  --blue:#1e88d8;
  --ad:#80b4f0;
  --pink:#ef1c86;
  --footer:#000;
  --footer-base:#0f1b1f;
  --footer-text:#9a9a9a;
  --line:#d8d8d8;
}
*{box-sizing:border-box;margin:0;padding:0}
html,body{width:809px;height:1200px;overflow:hidden;background:#fff}
body{position:relative;font-family:"Open Sans",Arial,sans-serif;color:var(--ink)}

/* header */
.site-header{position:absolute;left:0;top:0;width:809px;height:48px;background:var(--black);border-bottom:3px solid #cfcfcf}
.brand{position:absolute;left:92px;top:11px;display:flex;align-items:center;gap:7px}
.brand-mark{width:22px;height:22px;background:var(--teal)}
.brand-name{color:#fff;font-weight:700;font-size:12px;line-height:12px;width:110px}
.main-nav{position:absolute;top:0;left:319px;height:48px;display:flex;align-items:center}
.main-nav a{color:#fff;text-decoration:none;font-size:9.5px;font-weight:600;position:absolute;white-space:nowrap}
.caret{display:inline-block;border:3px solid transparent;border-top:4px solid #fff;margin-left:4px;vertical-align:-1px}

/* hero */
.hero{position:absolute;left:90px;top:82px;width:628px;height:232px;background:linear-gradient(135deg,#19d7de 0%,#0fbcd3 40%,#28d2e2 70%,#12b3cc 100%);overflow:hidden}
.hero-shadow{position:absolute;left:90px;top:314px;width:628px;height:6px;background:linear-gradient(#d9d9d9,#fff)}
.hero-band{position:absolute;left:0;top:42px;width:354px;height:40px;background:rgba(12,110,120,.75);padding:4px 0 0 14px}
.hero-band h1{color:#fff;font-size:19.5px;font-weight:800;line-height:22px;letter-spacing:-.5px;white-space:nowrap}
.hero-band p{color:#fff;font-size:10.5px;font-weight:700;line-height:12px;white-space:nowrap}
.hero-photo{position:absolute;left:36px;top:102px;width:306px;height:130px;background:radial-gradient(ellipse at 50% 70%,#b8835a 0%,#8d6444 45%,rgba(60,150,160,0) 75%)}
.policy-box{position:absolute;left:380px;top:8px;width:232px;height:216px;background:linear-gradient(160deg,#4dcfd6,#2aa7b0 60%,#237f88);border:3px solid #7ee4e8;padding:22px 12px 0 15px}
.policy-box h2{color:#1d4a54;font-size:17.5px;font-weight:800;line-height:20px;letter-spacing:-.4px;white-space:nowrap}
.policy-box p{color:#1d4a54;font-size:8px;font-weight:600;line-height:10px;margin-top:2px;width:200px}
.select{position:absolute;left:15px;width:198px;height:25px;background:#fff;border:1px solid #9fb8bb;font-size:8.5px;color:#555;padding:6px 0 0 9px}
.select::after{content:"";position:absolute;right:0;top:0;width:26px;height:23px;background:#d6d6d6;border-left:1px solid #b9b9b9}
.select::before{content:"";position:absolute;right:8px;top:9px;border:5px solid transparent;border-top:6px solid #555;z-index:1}
.continue{position:absolute;left:76px;top:162px;width:84px;height:20px;background:var(--pink);color:#fff;font-size:11.5px;font-weight:800;text-align:center;line-height:20px}
.continue::after{content:"";position:absolute;left:34px;top:20px;border:8px solid transparent;border-top:6px solid var(--pink)}
.dots{position:absolute;left:383px;top:335px;display:flex;gap:4px}
.dots i{width:7px;height:7px;border-radius:50%;background:#8b8b8b}
.dots i:first-child{background:var(--cyan)}

/* lists */
.list-panel{position:absolute;top:350px;width:189px}
.list-head{position:relative;height:46px;background:linear-gradient(#fff,#f0f0f0)}
.list-icon{position:absolute;left:2px;top:0;width:40px;height:44px;background:linear-gradient(#e0e0e0,#b9b9b9);border-radius:3px}
.list-icon.trophy{background:linear-gradient(#f5d56a,#b58a1e);width:30px;left:8px}
.list-head h3{position:absolute;left:45px;top:18px;font-size:15.5px;font-weight:400;color:#222;letter-spacing:.2px;white-space:nowrap}
.list-rows{list-style:none;box-shadow:0 8px 8px -6px #bbb}
.list-rows li{position:relative;height:38.4px;border-bottom:1px dashed var(--line);padding:8px 0 0 12px;font-size:8.5px;line-height:12px;color:#222}
.list-rows li:last-child{border-bottom:0}
.list-rows li::before{content:"";position:absolute;left:0;top:6px;width:3px;height:24px;background:var(--c)}
.go{position:absolute;right:6px;top:8px;width:21px;height:21px;border-radius:50%;background:#e4e4e4;border:1px solid #d4d4d4}
.go::after{content:"";position:absolute;left:5px;top:6px;width:6px;height:6px;border-top:2px solid #fff;border-right:2px solid #fff;transform:rotate(45deg)}
.go.on{background:var(--teal);border-color:var(--teal)}

/* posts */
.post{position:absolute;width:192px;height:140px;border-bottom:1px solid #eee;box-shadow:0 8px 6px -6px #ddd}
.post-meta{font-size:8.5px;color:#999;font-style:italic;white-space:nowrap}
.post-date{display:inline-block;width:43px;height:17px;background:var(--blue);color:#fff;font-style:normal;font-weight:700;font-size:7.5px;text-align:center;line-height:17px;margin-right:6px}
.post-meta b{color:#222;font-weight:700}
.post h4{font-family:Arial,Helvetica,sans-serif;font-size:15.5px;line-height:19px;font-weight:700;margin-top:9px;color:#111;letter-spacing:-.3px}
.post-thumb{position:absolute;left:0;top:74px;width:52px;height:52px;background:#e6e6e6}
.post-text{position:absolute;left:62px;top:74px;width:128px;font-size:7.5px;line-height:15px;color:#666}

/* sidebar */
.ad-space{position:absolute;left:548px;top:665px;width:159px;height:158px;background:var(--ad);color:#1b3c8c;font-family:Arial,sans-serif;font-size:12px;text-align:center;padding-top:66px;line-height:13px}
.tabs{position:absolute;left:554px;top:835px;display:flex;gap:2px}
.tabs span{display:block;width:70px;height:17px;background:linear-gradient(#f2f2f2,#d2d2d2);font-size:8px;font-weight:700;text-align:center;line-height:17px;color:#333;border-radius:6px 6px 0 0}
.widget{position:absolute;left:546px;top:852px;width:164px;height:130px;background:#e2e2e2;padding:5px}
.widget-inner{width:100%;height:100%;background:#fff;border:1px solid #c5c5c5;position:relative;font-family:Arial,sans-serif;font-size:7px;color:#333;padding:0 6px}
.widget-inner h5{font-size:8.5px;font-weight:700;border-bottom:1px solid #ddd;padding:4px 0 5px 6px;margin:0 -6px 6px;background:#f3f5fa}
.widget-inner p{line-height:9px;margin-bottom:5px}
.widget-inner a{color:#3b5998;text-decoration:none}
.widget-foot{position:absolute;left:6px;bottom:3px;right:6px;border-top:1px solid #ddd;padding-top:3px;font-size:6.5px;display:flex;align-items:center;gap:3px}
.widget-foot i{width:8px;height:8px;background:#3b5998}

/* footer */
.site-footer{position:absolute;left:0;top:1008px;width:809px;height:162px;background:var(--footer)}
.foot-col{position:absolute;top:16px}
.foot-col h6{color:#fff;font-size:16px;font-weight:400;margin-bottom:5px;white-space:nowrap}
.foot-col p{color:var(--footer-text);font-size:8.2px;line-height:12.5px;width:158px}
.foot-col ul{list-style:none}
.foot-col li{color:var(--footer-text);font-size:8.2px;line-height:17px;padding-left:13px;position:relative;white-space:nowrap}
.foot-col li::before{content:"";position:absolute;left:1px;top:7px;width:3px;height:3px;border-radius:50%;background:#555}
.foot-base{position:absolute;left:0;top:1170px;width:809px;height:30px;background:var(--footer-base);color:#fff;font-size:7.5px;font-weight:600}
.foot-base nav{position:absolute;left:101px;top:10px;display:flex;gap:14px}
.foot-base .copy{position:absolute;left:545px;top:10px}
</style>
</head>
<body>

<header class="site-header">
  <div class="brand"><span class="brand-mark"></span><span class="brand-name">Furrow Cover Polls UK</span></div>
  <nav class="main-nav">
    <a style="left:0">Home</a>
    <a style="left:48px">Policies<span class="caret"></span></a>
    <a style="left:113px">Glossary</a>
    <a style="left:172px">Fact Sheets</a>
    <a style="left:241px">Survey Reports</a>
    <a style="left:325px">News &amp; Comment</a>
  </nav>
</header>

<section class="hero">
  <div class="hero-photo" role="img" aria-label="Photo of dogs and cats sitting in a row"></div>
  <div class="hero-band">
    <h1>LOREM IPSUM DOLOR SIT AMET</h1>
    <p>LOREM IPSUM DOLOR SIT AMET, CONSECTETUER</p>
  </div>
  <form class="policy-box">
    <h2>CHECK OUT A POLICY</h2>
    <p>Lorem ipsum dolor sit amet, consectetur adipisicing elit, sed do eiusmod tempor.</p>
    <div class="select" style="top:88px">- Select a Company -</div>
    <div class="select" style="top:119px">- Select Policy -</div>
    <div class="continue">CONTINUE</div>
  </form>
</section>
<div class="hero-shadow"></div>
<div class="dots"><i></i><i></i><i></i><i></i><i></i></div>

<section class="list-panel" style="left:90px">
  <div class="list-head"><span class="list-icon" role="img" aria-label="Notepad and pen icon"></span><h3>MENU LIST</h3></div>
  <ul class="list-rows">
    <li style="--c:var(--teal)">Lorem ipsum dolor sit amet,<br>consectetuer adipiscing elit.<span class="go on"></span></li>
    <li style="--c:var(--cyan)">Lorem ipsum dolor sit amet,<br>consectetuer adipiscing elit.<span class="go"></span></li>
    <li style="--c:var(--magenta)">Lorem ipsum dolor sit amet,<br>consectetuer adipiscing elit.<span class="go"></span></li>
    <li style="--c:var(--orange)">Lorem ipsum dolor sit amet,<br>consectetuer adipiscing elit.<span class="go"></span></li>
    <li style="--c:var(--grey)">Lorem ipsum dolor sit amet,<br>consectetuer adipiscing elit.<span class="go"></span></li>
    <li style="--c:var(--dark)">Lorem ipsum dolor sit amet,<br>consectetuer adipiscing elit.<span class="go"></span></li>
  </ul>
</section>

<section class="list-panel" style="left:310px">
  <div class="list-head"><span class="list-icon trophy" role="img" aria-label="Trophy icon"></span><h3>POPULAR REVIEWS</h3></div>
  <ul class="list-rows">
    <li style="--c:var(--teal)">Lorem ipsum dolor sit amet,<br>consectetuer adipiscing elit.<span class="go on"></span></li>
    <li style="--c:var(--cyan)">Lorem ipsum dolor sit amet,<br>consectetuer adipiscing elit.<span class="go"></span></li>
    <li style="--c:var(--magenta)">Lorem ipsum dolor sit amet,<br>consectetuer adipiscing elit.<span class="go"></span></li>
    <li style="--c:var(--orange)">Lorem ipsum dolor sit amet,<br>consectetuer adipiscing elit.<span class="go"></span></li>
    <li style="--c:var(--grey)">Lorem ipsum dolor sit amet,<br>consectetuer adipiscing elit.<span class="go"></span></li>
    <li style="--c:var(--dark)">Lorem ipsum dolor sit amet,<br>consectetuer adipiscing elit.<span class="go"></span></li>
  </ul>
</section>

<section class="list-panel" style="left:530px">
  <div class="list-head"><span class="list-icon" role="img" aria-label="Checklist icon"></span><h3>LATEST REVIEWS</h3></div>
  <ul class="list-rows">
    <li style="--c:var(--teal)">Lorem ipsum dolor sit amet,<br>consectetuer adipiscing elit.<span class="go on"></span></li>
    <li style="--c:var(--cyan)">Lorem ipsum dolor sit amet,<br>consectetuer adipiscing elit.<span class="go"></span></li>
    <li style="--c:var(--magenta)">Lorem ipsum dolor sit amet,<br>consectetuer adipiscing elit.<span class="go"></span></li>
    <li style="--c:var(--orange)">Lorem ipsum dolor sit amet,<br>consectetuer adipiscing elit.<span class="go"></span></li>
    <li style="--c:var(--grey)">Lorem ipsum dolor sit amet,<br>consectetuer adipiscing elit.<span class="go"></span></li>
    <li style="--c:var(--dark)">Lorem ipsum dolor sit amet,<br>consectetuer adipiscing elit.<span class="go"></span></li>
  </ul>
</section>

<article class="post" style="left:90px;top:667px">
  <div class="post-meta"><span class="post-date">AUG 28, 09</span>Posted by Admin | <b>5 comments</b></div>
  <h4>Ut vitae magna eget purus viverra interdum</h4>
  <div class="post-thumb"></div>
  <p class="post-text">Ut vitae magna eget purus viverra interdum. Donec elit augue, pulvinar at, sagittis id, rutrum a, felis. Ut sit</p>
</article>
<article class="post" style="left:310px;top:667px">
  <div class="post-meta"><span class="post-date">AUG 28, 09</span>Posted by Admin | <b>5 comments</b></div>
  <h4>Ut vitae magna eget purus viverra interdum</h4>
  <div class="post-thumb"></div>
  <p class="post-text">Ut vitae magna eget purus viverra interdum. Donec elit augue, pulvinar at, sagittis id, rutrum a, felis. Ut sit</p>
</article>
<article class="post" style="left:90px;top:827px">
  <div class="post-meta"><span class="post-date">AUG 28, 09</span>Posted by Admin | <b>5 comments</b></div>
  <h4>Ut vitae magna eget purus viverra interdum</h4>
  <div class="post-thumb"></div>
  <p class="post-text">Ut vitae magna eget purus viverra interdum. Donec elit augue, pulvinar at, sagittis id, rutrum a, felis. Ut sit</p>
</article>
<article class="post" style="left:310px;top:827px">
  <div class="post-meta"><span class="post-date">AUG 28, 09</span>Posted by Admin | <b>5 comments</b></div>
  <h4>Ut vitae magna eget purus viverra interdum</h4>
  <div class="post-thumb"></div>
  <p class="post-text">Ut vitae magna eget purus viverra interdum. Donec elit augue, pulvinar at, sagittis id, rutrum a, felis. Ut sit</p>
</article>

<aside>
  <div class="ad-space">Advertising<br>Space</div>
  <div class="tabs"><span>CHATTERBOOK</span><span>CHIRPER</span></div>
  <div class="widget">
    <div class="widget-inner">
      <h5>Recent Activity</h5>
      <p>No recent activity to display.</p>
      <p>Put some Like buttons on your website to engage your users. Details can be found <a>here</a>.</p>
      <div class="widget-foot"><i></i>Chatterbook social plugin</div>
    </div>
  </div>
</aside>

<footer class="site-footer">
  <div class="foot-col" style="left:101px">
    <h6>Who We Are</h6>
    <p>Rhoncus quis, varius sed velis. Mauris quis nunc eu nunc molestie egestas et sit amet odio. Morbi lacinia velit in nibh sodales sed pharetra sem feugiat. Vivamus ut cursus augue. Integer sit amet arcu lorem, at egestas tellus. Phasellus tellus orci, congue at tristique at, mattis ut arcu.</p>
  </div>
  <div class="foot-col" style="left:320px">
    <h6>Custom Text Widget</h6>
    <ul>
      <li>Rhoncus quis varius sed velit nibh moles</li>
      <li>Mauris quis nunc eu nunc molestie</li>
      <li>Egestas et sit amet odio morbi quis nunc</li>
      <li>Lacinia velit in nibh sodales sed quis nunc</li>
      <li>Pharetra sem feugiat nibh sodales sed</li>
      <li>Vivamus ut cursus augue nibh sodales sed</li>
    </ul>
  </div>
  <div class="foot-col" style="left:545px">
    <h6>Custom Text Widget</h6>
    <ul>
      <li>Rhoncus quis varius sed velit nibh moles</li>
      <li>Mauris quis nunc eu nunc molestie</li>
      <li>Egestas et sit amet odio morbi quis nunc</li>
      <li>Lacinia velit in nibh sodales sed quis nunc</li>
      <li>Pharetra sem feugiat nibh sodales sed</li>
      <li>Vivamus ut cursus augue nibh sodales sed</li>
    </ul>
  </div>
</footer>
<div class="foot-base">
  <nav><span>Privacy Policy</span><span>Legal</span><span>About Furrow Cover Polls UK</span></nav>
  <span class="copy">Copyright Kilnmark Studio 2013 / &nbsp;All Rights Reserved.</span>
</div>

</body>
</html>
```